Advertising tiles for website

Hi
I have a website at www.tagwhistle.co.nz and there are four spots along the top for advertising tiles (at the moment there are dummy tiles in place).

Each tile is 220 wide and 200 high and I would like 4 tiles created as a starting point for this site.

I can change the tiles on every page so conceivably we could have very targeted advertising leading the visitor to services we want to promote (we can set this extension up as a new design job for you). Eg. domains for sale, Escrow services, featured domains, Turnkey Websites, New Websites etc.

The advertisements that I might like see on the website would be as follows:
Gallery Ink
Sell Your Domain
Domains For Sale
Featured Domains
Buy Websites
Sell Your Website
Turnkey Websites
Trusted Escrow
New domains
News
Resources
note: the deliverable for this job is 4 tiles (not all of the above)as I want to get the design style sorted with you.

The website where these will appear sells pre-loved domains and turnkey websites. Also, some of these tiles will link through to a classifieds website which we will also want you to help create tiles for once this job is completed to satisfaction.

The files attached are samples only.

Target Market(s)

Domain buyers
Business owners
People buying websites

Industry/Entity Type

Advertising

Requirements
Must have
• Nice clean, clear text
Relevant
Nice to have
• Fun

```html
<!DOCTYPE html>
<html lang="en">
<head>
<meta charset="utf-8">
<title>Tagwhistle.co.nz – Premium Domains &amp; Websites</title>
<link href="https://fonts.googleapis.com/css2?family=Arimo:wght@400;700&display=swap" rel="stylesheet">
<style>
  :root{
    --red:#a50f15;
    --red-dark:#7a0608;
    --red-light:#c62a2f;
    --maroon:#6e0a0a;
    --text:#555;
    --link:#9b0a0a;
    --white:#fff;
    --rule:#c8c8c8;
  }
  *{box-sizing:border-box;margin:0;padding:0}
  html,body{width:1200px;height:900px;overflow:hidden;background:var(--white);font-family:Arimo,Arial,sans-serif}
  .page{position:relative;width:1200px;height:900px}
  .utility-bar{position:absolute;left:50px;top:50px;width:1100px;height:33px;background:linear-gradient(var(--red-light),var(--red-dark));display:flex;justify-content:flex-end;align-items:center;padding-right:65px}
  .utility-bar a{color:#f3dcdc;font-size:11px;text-decoration:none;padding:0 11px;border-left:1px solid rgba(255,255,255,.3);line-height:33px}
  .utility-bar a:last-child{border-right:1px solid rgba(255,255,255,.3)}
  .side-shade{position:absolute;left:50px;top:249px;width:1100px;height:80px;background:linear-gradient(#e4e4e4,#fff)}
  .sheet{position:absolute;left:110px;top:83px;width:980px;height:817px;background:var(--white);box-shadow:0 0 4px rgba(0,0,0,.15)}
  .masthead{position:absolute;left:118px;top:90px;width:966px;height:122px;background:linear-gradient(#fff,#e6e6e6);border:1px solid #ddd}
  .masthead-art{position:absolute;left:0;top:0;width:328px;height:120px;background:linear-gradient(135deg,#e8e8e8,#cfcfcf 60%,#c4c4c4)}
  .brand-name{position:absolute;right:14px;bottom:14px;font-size:30px;font-weight:700;color:var(--red)}
  .main-nav{position:absolute;left:50px;top:217px;width:1100px;height:32px;background:linear-gradient(var(--red-light),var(--red-dark));display:flex;padding-left:84px}
  .main-nav a{color:var(--white);font-weight:700;font-size:13.5px;text-decoration:none;line-height:32px;margin-right:36px}
  .tiles{position:absolute;left:170px;top:268px;display:flex;gap:10px}
  .tile{width:208px;height:192px;border-radius:8px;background:linear-gradient(#d44a4e,#b6151c 45%,#a10e14);box-shadow:0 3px 4px rgba(0,0,0,.4);border:1px solid #7a0608;position:relative;color:var(--white);text-align:center;font-weight:700}
  .tile-title{position:absolute;top:12px;width:100%;font-size:19px}
  .tile-sub{position:absolute;bottom:14px;width:100%;font-size:15px}
  .tile svg{position:absolute;left:46px;top:38px}
  .content{position:absolute;left:126px;top:480px;width:946px;color:var(--text);font-size:12px}
  h1{color:var(--maroon);font-size:20px;margin-bottom:14px}
  h2{color:var(--red);font-size:16px;margin-bottom:16px}
  .quote,.content ul,.content p{letter-spacing:.3px}
  .quote{margin-bottom:10px}
  .quote em{font-weight:700}
  ul{margin-left:40px;list-style:disc;line-height:13px}
  a.inline{color:var(--link)}
  .rule{border-top:2px dashed var(--rule);margin:8px 0}
  .big{color:var(--maroon);font-size:20px;font-weight:700;line-height:25px;margin:8px 0 16px;letter-spacing:-.2px}
  .big a{color:var(--red)}
  p{margin-bottom:11px;line-height:14px}
</style>
</head>
<body>
<div class="page">
  <div class="side-shade"></div>
  <div class="sheet"></div>
  <nav class="utility-bar">
    <a href="#">Home</a><a href="#">Bookmark Site</a><a href="#">Print</a><a href="#">Tell a Friend</a><a href="#">Contact Us</a>
  </nav>
  <header class="masthead">
    <div class="masthead-art" role="img" aria-label="Illustration of small figures climbing large red WWW letters"></div>
    <span class="brand-name">Tagwhistle</span>
  </header>
  <nav class="main-nav">
    <a href="#">Home</a><a href="#">Recent Sales</a><a href="#">Search Listings</a><a href="#">Register New Domain</a><a href="#">Escrow</a><a href="#">FAQ</a><a href="#">Contact Us</a>
  </nav>
  <section class="tiles">
    <div class="tile"><div class="tile-title">BUY</div>
      <svg width="116" height="116"><circle cx="58" cy="58" r="56" fill="none" stroke="#fff" stroke-width="2"/><circle cx="58" cy="58" r="36" fill="none" stroke="#fff" stroke-width="6"/><text x="58" y="76" text-anchor="middle" font-size="48" font-weight="700" fill="#fff" font-family="Arimo,sans-serif">$</text></svg>
      <div class="tile-sub">A WEBSITE</div></div>
    <div class="tile"><div class="tile-title">TRUSTED</div>
      <svg width="116" height="116"><circle cx="58" cy="58" r="56" fill="none" stroke="#fff" stroke-width="2"/><path d="M58 92 L26 58 A17 17 0 0 1 58 36 A17 17 0 0 1 90 58 Z" fill="#fff"/></svg>
      <div class="tile-sub">ESCROWS AVAILABLE</div></div>
    <div class="tile"><div class="tile-title">NEWS</div>
      <svg width="116" height="116"><circle cx="58" cy="58" r="56" fill="none" stroke="#fff" stroke-width="2"/><rect x="30" y="36" width="56" height="44" fill="#fff"/><rect x="36" y="42" width="44" height="8" fill="#b6151c"/><rect x="36" y="54" width="20" height="20" fill="#b6151c"/><rect x="60" y="54" width="20" height="4" fill="#b6151c"/><rect x="60" y="62" width="20" height="4" fill="#b6151c"/><rect x="60" y="70" width="20" height="4" fill="#b6151c"/></svg>
      <div class="tile-sub">DOMAINS</div></div>
    <div class="tile"><div class="tile-title">SELL</div>
      <svg width="116" height="116"><circle cx="58" cy="58" r="56" fill="none" stroke="#fff" stroke-width="2"/><g fill="none" stroke="#fff" stroke-width="6" stroke-linecap="round"><path d="M24 46 A48 48 0 0 1 92 46"/><path d="M34 58 A34 34 0 0 1 82 58"/><path d="M44 70 A20 20 0 0 1 72 70"/></g><text x="58" y="96" text-anchor="middle" font-size="20" font-weight="700" fill="#fff" font-family="Arimo,sans-serif">$</text></svg>
      <div class="tile-sub">YOUR WEBSITE</div></div>
  </section>
  <main class="content">
    <h1>Tagwhistle.co.nz Ranked #1 on Findly NZ Search</h1>
    <h2>Selling Premium Domains &amp; Websites Since 2003</h2>
    <p class="quote">"<em>Domains have and will continue to go up in value faster than any other commodity EVER known to man.</em>" Grant Hollis, Hollis Software Ltd</p>
    <ul>
      <li><a class="inline" href="#">Browse listings in alphabetical order</a></li>
      <li><a class="inline" href="#">Browse listings in price order</a></li>
      <li>Looking for something suitable to your industry or interests? <a class="inline" href="#">Browse listings in category order</a></li>
      <li>Like to know how much domains have been selling for?&nbsp; Check out <a class="inline" href="#">2010 top international sales</a> and <a class="inline" href="#">some of NZ's sales</a></li>
    </ul>
    <div class="rule"></div>
    <div class="big">Domain names are virtual real estate and hugely valuable.&nbsp; Check out some <a href="#">recent sales </a>and the <a href="#">top 100 sales</a></div>
    <ul>
      <li>Your domain name greatly influences search engine results.</li>
      <li>You can <a class="inline" href="#">buy premium domain names</a> on this site and buy existing websites and online businesses already set up ready to go.</li>
      <li>Search and <a class="inline" href="#">register new domains</a> with Open Lot.</li>
    </ul>
    <div class="rule"></div>
    <p>There are now 415,000 registered New Zealand domains with businesses realising the importance of brand protection as well as the investment opportunities offered by <b>virtual real estate.</b> (NZ <i>Domain Registry Office</i>)</p>
    <p>Improve your brand - Improve Search Engine Results - Domains Are An Investment In Success</p>
    <p>All prices are gst inclusive and offers are welcome</p>
  </main>
</div>
</body>
</html>
```